Improved Business Card, Government Contracting

We are looking to update the design of our business cards. We would like to create a template that can be used for future employees and easy to update.

Halvorsen Advisory Partners, LLC is a Service Disabled Veteran Owned Small Business with headquarters located in Leavenworth, KS. Our current website is www.hapteam.com. We have contracts in KS and VA with expansion opportunities in various other states. Our primary line of work is within government contracting and providing consulting services to various organizations within the Bureau of Frontier Works. We would like to project a professional image of our company that is consistent with the industry. Provided are previous versions of our business card template that shows our logo as well. We would like to make sure the information on the cards are easily noticeable .

Target Market(s)

Government Officials
Fellow Small Business Contractors
Large Business Contractors (ex. TRUX, Keswell Barnaby, Pryde Okonjo Whitcombe)

Industry/Entity Type

Business

Contact Information for Business Card

Dale Fenwick
Office Manager
Halvorsen Advisory Partners
Ph: 555.555.0172
Email: d.fenwick@hapteam.us
www.hapteam.com

Requirements
Must have
• The business mailing address is:
• 31842 204th Lane
• Fernhollow, WR 66099
Nice to have
• Embossed lettering

```html
<!DOCTYPE html>
<html lang="en">
<head>
<meta charset="utf-8">
<title>Halvorsen Advisory Partners – Business Card</title>
<link href="https://fonts.googleapis.com/css2?family=Open+Sans:wght@400;600;700&display=swap" rel="stylesheet">
<style>
  :root {
    --backdrop: #2b2b2b;
    --brand-blue: #4a60a9;
    --brand-yellow: #fbf163;
    --brand-yellow-deep: #ece04a;
    --paper-white: #ffffff;
  }
  * { box-sizing: border-box; margin: 0; padding: 0; }
  html, body {
    width: 1200px;
    height: 830px;
    overflow: hidden;
  }
  body {
    background: var(--backdrop);
    font-family: "Open Sans", Arial, sans-serif;
    position: relative;
  }
  .card {
    position: absolute;
    left: 380px;
    width: 441px;
    height: 271px;
    overflow: hidden;
  }

  /* Front side */
  .card--front {
    top: 110px;
    background: var(--brand-blue);
    color: var(--paper-white);
  }
  .chevron-art {
    position: absolute;
    left: 0;
    top: 0;
    width: 441px;
    height: 271px;
  }
  .front-wordmark {
    position: absolute;
    left: 232px;
    top: 36px;
    width: 200px;
    text-align: center;
    color: var(--brand-yellow);
    font-weight: 600;
    line-height: 1.1;
  }
  .front-wordmark__main { display: block; font-size: 22px; letter-spacing: 0.5px; }
  .front-wordmark__sub { display: block; font-size: 12px; letter-spacing: 0.6px; }

  .contact {
    position: absolute;
    right: 16px;
    top: 124px;
    width: 160px;
    text-align: right;
  }
  .contact__name {
    font-size: 20px;
    font-weight: 600;
    line-height: 24px;
    padding-bottom: 3px;
    border-bottom: 1.5px solid var(--paper-white);
  }
  .contact__company,
  .contact__role {
    font-size: 6.5px;
    font-weight: 700;
    line-height: 9px;
    text-transform: uppercase;
  }
  .contact__company { margin-top: 6px; }
  .contact__details {
    margin-top: 12px;
    font-size: 7.5px;
    line-height: 10.5px;
    font-weight: 400;
  }
  .contact__details .gap { margin-top: 3px; }

  /* Back side */
  .card--back {
    top: 427px;
    background: var(--brand-yellow);
    display: flex;
    align-items: center;
    justify-content: center;
  }
  .back-wordmark {
    text-align: center;
    color: var(--brand-blue);
    font-weight: 600;
    line-height: 1.1;
  }
  .back-wordmark__main { display: block; font-size: 36px; letter-spacing: 1px; }
  .back-wordmark__sub { display: block; font-size: 19px; letter-spacing: 1.5px; }
</style>
</head>
<body>

  <section class="card card--front" aria-label="Business card front">
    <svg class="chevron-art" viewBox="0 0 441 271" aria-hidden="true">
      <polygon points="0,0 48,0 220,136 48,271 0,271" fill="var(--brand-yellow)"/>
      <polygon points="0,0 48,0 30,14 0,14" fill="var(--brand-yellow-deep)"/>
      <polygon points="0,271 48,271 30,257 0,257" fill="var(--brand-yellow-deep)"/>
      <polygon points="0,30 153,136 0,242" fill="var(--paper-white)"/>
    </svg>

    <div class="front-wordmark">
      <span class="front-wordmark__main">HALVORSEN</span>
      <span class="front-wordmark__sub">ADVISORY PARTNERS</span>
    </div>

    <div class="contact">
      <p class="contact__name">Dale Fenwick</p>
      <p class="contact__company">Halvorsen Advisory Partners</p>
      <p class="contact__role">Office Manager</p>
      <div class="contact__details">
        <p>Ph: 555.555.0172</p>
        <p class="gap">31842 204th Lane</p>
        <p>Fernhollow, WR 66099</p>
        <p>Email : d.fenwick@hapteam.us</p>
        <p class="gap">Website : www.hapteam.com</p>
      </div>
    </div>
  </section>

  <section class="card card--back" aria-label="Business card back">
    <div class="back-wordmark">
      <span class="back-wordmark__main">HALVORSEN</span>
      <span class="back-wordmark__sub">ADVISORY PARTNERS</span>
    </div>
  </section>

</body>
</html>
```